Design a Professional Stationery

Hi everyone,
I would like to make a design of stationery for my company Corvel Wrap (www.corvelwrap-example.com).
General Info: We are manufacturers of packaging supplies (poly bubble mailers, kraft bubble mailers, bubble wrap, tape, stretch film). We have couple of big warehouses in Los Angeles and New Jersey that serves East and West Coasts. We store lot of boxes with our product. We are wholesalers so we work with big serious distributors.

Project Goals: Create a business stationery that will look professional, modern and straight to the point. Colors: Dark blue, white, light blue (please see the web site). Blue is the color of success.
I want them to be presentable. As you might need to imagine my team will walk around the businesses and leave folders with information at clients table. We will distribute them at the trade shows, business meetings etc.

Target Market(s)

Business professionals looking for professional wholesaler manufacturer.

Industry/Entity Type

It Company

Font styles to use
Serif
Sans Serif

Colors
3276b5
0255a3
85acd3
cedeed
eaf1f7

Requirements
Must have
• People photos, product photos, add professional warehouse photos, truck, machinery.
Nice to have
• NLP
Should not have
• Use your imagination, no limits so far

```html
<!DOCTYPE html>
<html lang="en">
<head>
<meta charset="utf-8">
<title>Corvel Wrap – Business Card</title>
<link rel="stylesheet" href="https://fonts.googleapis.com/css2?family=Questrial&display=swap">
<style>
  :root{
    --navy:#0a2b5c;
    --blue:#3276b5;
    --blue-mid:#85acd3;
    --blue-light:#cedeed;
    --paper:#f7f9fc;
    --ink:#2a2f38;
    --backdrop:#e6e7ec;
  }
  *{margin:0;padding:0;box-sizing:border-box}
  html,body{width:1200px;height:934px;overflow:hidden;background:var(--backdrop);
    font-family:"Questrial",sans-serif;color:var(--ink)}
  .canvas{position:relative;width:1200px;height:934px}
  .card{position:absolute;left:340px;width:520px;height:297px;overflow:hidden;
    box-shadow:0 6px 18px rgba(20,30,60,.18)}
  .card--front{top:110px;background:var(--navy)}
  .card--back{top:507px;background:var(--paper)}

  .brand{display:flex;align-items:center;gap:10px;font-size:34px;letter-spacing:2px;text-transform:uppercase;line-height:1}
  .brand__mark{width:14px;height:14px;flex:none}
  .tagline{font-size:8px;letter-spacing:1.6px;text-transform:uppercase;margin-top:6px}

  .card--front .lockup{position:absolute;left:0;right:0;top:108px;display:flex;flex-direction:column;align-items:center}
  .card--front .brand{color:#fff}
  .card--front .brand__mark{background:#fff}
  .card--front .tagline{color:#fff}

  .stripe{position:absolute;left:0;right:0;bottom:0;height:12px;display:flex}
  .stripe span{height:100%}
  .s-navy{background:var(--navy)} .s-blue{background:var(--blue)}
  .s-mid{background:var(--blue-mid)} .s-light{background:var(--blue-light)}
  .card--front .stripe .s-navy{background:var(--navy)}

  .card--back .lockup{position:absolute;right:30px;top:34px;display:flex;flex-direction:column;align-items:flex-end}
  .card--back .brand{color:var(--navy);font-size:26px}
  .card--back .brand__mark{background:var(--navy);width:12px;height:12px}
  .card--back .tagline{color:var(--navy);font-size:7px}

  .person{position:absolute;left:34px;top:104px}
  .person__name{color:var(--blue);font-size:20px;letter-spacing:1px;text-transform:uppercase}
  .person__title{font-size:13px;margin-top:3px}

  .address{position:absolute;right:34px;top:142px;text-align:right;font-size:12.5px;line-height:1.45}

  .contacts{position:absolute;left:34px;bottom:32px;list-style:none;font-size:12.5px}
  .contacts li{display:flex;align-items:center;gap:9px;height:19px}
  .icon{width:15px;height:15px;flex:none}
</style>
</head>
<body>
<main class="canvas">

  <section class="card card--front" aria-label="Card front">
    <div class="lockup">
      <div class="brand"><span class="brand__mark"></span>Corvel Wrap</div>
      <div class="tagline">Shipping and Mailing Supply</div>
    </div>
    <div class="stripe">
      <span class="s-navy" style="width:36%"></span>
      <span class="s-blue" style="width:30%"></span>
      <span class="s-mid" style="width:34%"></span>
    </div>
  </section>

  <section class="card card--back" aria-label="Card back">
    <div class="lockup">
      <div class="brand"><span class="brand__mark"></span>Corvel Wrap</div>
      <div class="tagline">Shipping and Mailing Supply</div>
    </div>

    <div class="person">
      <div class="person__name">Jordan Mercer</div>
      <div class="person__title">General Manager</div>
    </div>

    <address class="address" style="font-style:normal">4200 Harlow Ave<br>Fenmore CA 90000</address>

    <ul class="contacts">
      <li>
        <svg class="icon" viewBox="0 0 16 16" aria-hidden="true"><rect width="16" height="16" rx="3" fill="#0a2b5c"/><path d="M5 3.5l2 2-1 1.2c.6 1.3 1.5 2.2 2.8 2.8l1.2-1 2 2-1.2 1.5C7.5 11.8 4.2 8.5 3.5 5.2z" fill="#fff"/></svg>
        555-014-2290
      </li>
      <li>
        <svg class="icon" viewBox="0 0 16 16" aria-hidden="true"><rect width="16" height="16" rx="3" fill="#0a2b5c"/><rect x="3.5" y="5" width="9" height="6.5" fill="none" stroke="#fff" stroke-width="1.1"/><path d="M3.5 5l4.5 3.6L12.5 5" fill="none" stroke="#fff" stroke-width="1.1"/></svg>
        info@corvelwrap-example.com
      </li>
      <li>
        <svg class="icon" viewBox="0 0 16 16" aria-hidden="true"><rect width="16" height="16" rx="3" fill="#0a2b5c"/><g fill="none" stroke="#fff" stroke-width="1"><circle cx="8" cy="8" r="4.5"/><ellipse cx="8" cy="8" rx="2" ry="4.5"/><path d="M3.5 8h9M4.3 5.7h7.4M4.3 10.3h7.4"/></g></svg>
        www.corvelwrap-example.com
      </li>
    </ul>

    <div class="stripe">
      <span class="s-navy" style="width:64%"></span>
      <span class="s-blue" style="width:9%"></span>
      <span class="s-mid" style="width:9%"></span>
      <span class="s-light" style="width:9%"></span>
      <span class="s-navy" style="width:9%"></span>
    </div>
  </section>

</main>
</body>
</html>
```